A Visual Masterpiece for an Optometry Practice

We are looking for a web designer to create a website for our optometry business that makes the client appreciate the gift of sight. We are looking for something clean and crisp but beautiful and compelling. Something that is unique and experiencial. So if you are up for the artistic challenge, lets journey together and create something amazing. We look forward to working with you!
Updates

I updated the source files for the logos. Thanks for letting me know that the other ones did not work. Thanks everyone!

I am extending the deadline due to the fact that there has only been a few submissions. This does not reflect the quality of the subissions, but we are looking for a larger pool to choose from. Thank you so much for your flexibility and patience. We appreciate you and the work you have done =)

Target Market(s)

This business is in Lancaster, Ohio which is mainly hosts mainly blue-colared families. We believe that a lot of times people do not come to an optometrist until something is wrong with their eyes, and we would love to change that. We want to bring awareness to how amazing the gift of sight is and want to focus on beauty, adventure and playfulness. With this being said, we want our website to be full of wonder, beauty and adventure. something that makes someone say, "check this out! This is freaking amazing!"

Industry/Entity Type

Business

Requirements
Must have
• Home Page
Location Page
Contact Page
"Register Online" Page
Philophy Page
Stories page (simular to a testimonial)

We would like it to be very user friendly and able to be updated easily by one of our nurses

also, I have uploaed source files of our logo for you to insert on each page.

If you have ideas or concepts that would include actual photos of the doctor or day to day activities, we can hire a photographer for quality images. We didnt want to do that prior to picking the designer.
Nice to have
• We would love it to feel simple but at the same time full of life. Wed love for the site to take the eye on a journey.

```html
<!DOCTYPE html>
<html lang="en">
<head>
<meta charset="utf-8">
<title>Brightfield Optometry</title>
<link href="https://fonts.googleapis.com/css2?family=Noto+Sans:ital,wght@0,400;0,700;1,700&display=swap" rel="stylesheet">
<style>
:root{
  --green-dark:#0f5a2f;
  --green-nav:#17703a;
  --green-nav-2:#0c5a2b;
  --sky:#cfe8f4;
  --hill:#8cc63f;
  --cyan:#19b6e8;
  --cyan-light:#7fd8f3;
  --card:#e9edf2;
  --text:#2b2b2b;
  --lime-1:#b2e02a;
  --lime-2:#7cbd12;
  --lime-text:#1e5b17;
  --orange-1:#fbb040;
  --orange-2:#f47b10;
  --orange-text:#5a2d05;
  --blue-1:#63c0f2;
  --blue-2:#2b8fd4;
  --footer:#0a5874;
  --footer-link:#4fd0f5;
  --white:#ffffff;
  --slate:#3b4144;
}
*{box-sizing:border-box;margin:0;padding:0}
html,body{width:929px;height:1200px;overflow:hidden}
body{position:relative;background:var(--white);font-family:"Noto Sans",Arial,sans-serif;color:var(--text)}
.abs{position:absolute}

/* header */
.header-sky{left:0;top:0;width:929px;height:210px;background:linear-gradient(180deg,#bfe1f2 0%,#eaf5fa 45%,#f6fbef 75%,var(--hill) 100%)}
.register-tab{left:690px;top:0;width:210px;height:43px;background:linear-gradient(#5b6366,var(--slate));color:#fff;font-size:16px;letter-spacing:.5px;display:flex;align-items:center;justify-content:center;border-radius:0 0 18px 18px}
.brand{left:50px;top:80px;display:flex;align-items:center;gap:14px}
.brand-mark{width:70px;height:70px;background:#9fcf6a}
.brand-name{font-size:42px;color:var(--green-dark);font-weight:400;line-height:1}
.phone{left:660px;top:100px;text-align:right;width:220px}
.phone-number{font-size:25px;font-weight:700;color:#222}
.phone-note{font-size:13px;font-weight:700;color:#111}

/* nav */
.nav{left:0;top:210px;width:929px;height:46px;background:linear-gradient(var(--green-nav),var(--green-nav-2));border-top:2px solid #2f8a4e;display:flex;padding-left:42px}
.nav a{color:#fff;font-size:13px;text-decoration:none;display:flex;align-items:center;justify-content:center;border-right:1px solid #3c8a57}
.nav a.active{background:#222}

/* hero */
.hero-band{left:0;top:256px;width:929px;height:354px;background:linear-gradient(90deg,var(--cyan) 0%,var(--cyan-light) 50%,var(--cyan) 100%)}
.hero-card{left:42px;top:267px;width:851px;height:266px;background:linear-gradient(180deg,#f4f6f8,var(--card));border-radius:6px;overflow:hidden}
.hero-title{left:13px;top:14px;font-size:16px;color:#222}
.hero-title span{font-size:31px;color:var(--green-dark)}
.hero-text{left:14px;top:80px;width:360px;font-size:11.5px;line-height:18px;color:#222}
.read-more{left:12px;top:198px;width:170px;height:38px;border-radius:19px;background:linear-gradient(#5fc0fa,#1689e0);color:#0b3f7c;font-weight:700;font-style:italic;font-size:19px;display:flex;align-items:center;padding-left:20px}
.read-more svg{position:absolute;right:10px;top:9px}
.hero-photo{left:411px;top:0;width:440px;height:266px;background:linear-gradient(120deg,#d9dde2,#9aa3a8 55%,#6a7a5a)}
.share-bar{left:59px;top:533px;width:818px;height:44px;background:linear-gradient(#f4f6f8,#dde3e8);border-radius:0 0 14px 14px;display:flex;align-items:center;padding:0 20px;font-size:12px}
.share-btn{display:flex;gap:4px;margin-right:10px}
.share-btn span{background:#fff;border:1px solid #c9d3dc;border-radius:3px;padding:1px 5px;font-size:11px;color:#1c5a8a}
.get-touch{margin-left:48px;color:var(--green-dark);margin-right:14px}
.social{display:flex;gap:8px}
.social i{width:22px;height:22px;border-radius:50%;background:#2a6db5;display:block}
.social i:nth-child(2){background:#39a9e0}
.social i:nth-child(3){background:#1f6fa8}
.social i:nth-child(4){background:#c4302b;border-radius:3px}
.slider{margin-left:auto;display:flex;align-items:center;gap:5px}
.dot{width:12px;height:12px;border-radius:50%;background:#c8ced4;border:1px solid #9aa3aa}
.dot.on{background:#2f6d2a}
.arrow{width:20px;height:20px;border-radius:50%;background:#111;display:flex;align-items:center;justify-content:center}
.shadow-pad{left:59px;top:577px;width:818px;height:40px;background:linear-gradient(#e9edf0,#fff);border-radius:14px 14px 0 0}

/* feature boxes */
.box{top:618px;height:276px;border-radius:8px;padding:10px 14px;overflow:hidden}
.box h2{font-size:21px;font-weight:400;padding-bottom:10px;border-bottom:1px solid rgba(0,0,0,.12)}
.box-facilities{left:42px;width:275px;background:linear-gradient(var(--lime-1),var(--lime-2));border:1px solid #7fae18}
.box-facilities h2{color:var(--lime-text)}
.facility-list{list-style:none;margin-top:16px}
.facility-list li{font-size:11.5px;line-height:21.5px;color:#1a2a0a;padding-left:12px;position:relative}
.facility-list li:before{content:"";position:absolute;left:0;top:7px;border-left:5px solid #2d4a0c;border-top:4px solid transparent;border-bottom:4px solid transparent}
.btn{position:absolute;bottom:12px;height:25px;border-radius:5px;font-size:12px;display:flex;align-items:center;padding:0 12px;gap:8px}
.btn-facilities{left:22px;background:#3c8a1a;color:#c8ef8a;width:136px}
.box-diseases{left:342px;width:275px;background:linear-gradient(var(--orange-1),var(--orange-2));border:1px solid #e0801a}
.box-diseases h2{color:var(--orange-text)}
.disease-photo{margin-top:12px;height:80px;border-radius:6px;background:linear-gradient(90deg,#6b4fa3,#c8b7a8 55,#e7d3c2);background:linear-gradient(90deg,#6b4fa3 0%,#c9b3a6 55%,#ead6c4 100%);border:2px solid #fff}
.disease-text{margin-top:10px;font-size:11.5px;line-height:17px;color:#2a1500}
.btn-solutions{left:12px;background:linear-gradient(#fbb543,#f18a12);color:#5a2d05;width:136px;border:1px solid #fff3}
.box-doctor{left:640px;width:253px;background:linear-gradient(var(--blue-1),var(--blue-2));border:1px solid #2f8ccb}
.box-doctor h2{color:#111;border-bottom:none;padding-bottom:0}
.field{background:#fff;border-radius:7px;height:25px;margin-top:8px;font-size:10px;color:#9aa;padding:6px 12px}
.field.first{margin-top:14px}
.field.message{height:80px}
.btn-submit{left:14px;background:linear-gradient(#5ac0e8,#1a7cb0);color:#07324a;width:92px;border:1px solid #0f5a85}

/* footer */
.footer-tab{left:42px;top:914px;width:851px;height:60px;background:var(--footer);border-radius:22px 22px 0 0}
.footer{left:0;top:942px;width:929px;height:258px;background:var(--footer)}
.footer-col{top:930px;color:#fff}
.footer-col h3{font-size:14px;font-weight:400;margin-bottom:14px}
.quick-links{left:58px}
.quick-links ul{list-style:none}
.quick-links li{font-size:11.5px;line-height:21.5px;color:var(--footer-link);padding-left:12px;position:relative}
.quick-links li:before{content:"";position:absolute;left:0;top:9px;width:4px;height:4px;background:#fff;transform:rotate(45deg)}
.newsletter{left:315px;width:260px}
.news-field{background:#fff;border-radius:8px;height:24px;font-size:10px;color:#111;padding:5px 12px;margin-bottom:9px}
.news-text{font-size:11px;line-height:15px;color:var(--footer-link)}
.subscribe{margin-top:10px;width:163px;height:30px;border-radius:15px;background:linear-gradient(#7fd0f7,#2a8fd4);color:#0a2d4a;font-size:14px;display:flex;align-items:center;padding-left:14px;position:relative}
.subscribe svg{position:absolute;right:6px;top:5px}
.follow{left:673px}
.follow .social{gap:6px}
.follow .social i{width:36px;height:36px}
.contact-title{margin-top:18px}
.contact-line{display:flex;align-items:center;gap:12px;margin-top:6px;font-size:16px}
.contact-line.email{font-size:13px;margin-top:14px}
.footer-rule{left:42px;top:1160px;width:851px;height:1px;background:#2a7592}
.copyright{left:0;top:1173px;width:929px;text-align:center;color:#fff;font-size:10px}
</style>
</head>
<body>

<div class="abs header-sky" role="img" aria-label="Bright sky with soft clouds over a green grassy hill"></div>
<div class="abs register-tab">REGISTER ONLINE</div>
<div class="abs brand">
  <div class="brand-mark"></div>
  <div class="brand-name">Brightfield Optometry</div>
</div>
<div class="abs phone">
  <div class="phone-number">555.0100.234</div>
  <div class="phone-note">For Any Queries, Call Us</div>
</div>

<nav class="abs nav">
  <a class="active" style="width:92px">Home</a>
  <a style="width:106px">About Us</a>
  <a style="width:112px">Deseases</a>
  <a style="width:119px">Treatments</a>
  <a style="width:121px">Philosophy</a>
  <a style="width:95px">Stories</a>
  <a style="width:105px">Location</a>
  <a style="width:119px;border-right:none">Contact Us</a>
</nav>

<div class="abs hero-band"></div>
<div class="abs shadow-pad"></div>
<section class="abs hero-card">
  <div class="abs hero-title">Welcome to <span>Brightfield</span></div>
  <p class="abs hero-text">Lorem ipsum dolor sit amet, consectetur adipiscing elit. Nam consequat risus at lorem sodales imperdiet. Morbi dapibus, ipsum at elementum tincidunt, magna odio iaculis arcu, vitae elementum risus erat vitae lorem. Proin vel magna a arcu porttitor dignissim id sit amet lacus. Vestibulum in erat et orci rhoncus dignissim sed a nulla.</p>
  <div class="abs read-more">Read More
    <svg width="20" height="20" viewBox="0 0 20 20"><circle cx="10" cy="10" r="8.5" fill="none" stroke="#fff" stroke-width="2"/><path d="M6 10h7M10 6.5l3.5 3.5-3.5 3.5" fill="none" stroke="#fff" stroke-width="2"/></svg>
  </div>
  <div class="abs hero-photo" role="img" aria-label="Photo of a patient having an eye examination at a slit lamp"></div>
</section>
<div class="abs share-bar">
  <div class="share-btn"><span>Share</span><span>7,231</span></div>
  <div class="share-btn"><span>Like</span><span>7,231</span></div>
  <div class="get-touch">Get in touch</div>
  <div class="social"><i></i><i></i><i></i><i></i></div>
  <div class="slider">
    <div class="arrow"><svg width="10" height="10" viewBox="0 0 10 10"><path d="M6.5 1.5 3 5l3.5 3.5" fill="none" stroke="#fff" stroke-width="2"/></svg></div>
    <div class="dot on"></div><div class="dot"></div><div class="dot"></div><div class="dot"></div><div class="dot"></div>
    <div class="arrow"><svg width="10" height="10" viewBox="0 0 10 10"><path d="M3.5 1.5 7 5 3.5 8.5" fill="none" stroke="#fff" stroke-width="2"/></svg></div>
  </div>
</div>

<section class="abs box box-facilities">
  <h2>Facilities</h2>
  <ul class="facility-list">
    <li>Proin at dolor nunc, vel venenatis risus.</li>
    <li>In vel lorem quis nisl pulvinar dapibus.</li>
    <li>Duis non mauris erat, ac semper tortor.</li>
    <li>Donec et nulla ut lacus scelerisque dapibus.</li>
    <li>Curabitur vel ligula orci, quis dapibus nunc.</li>
    <li>Cras ultrices sollicitudin odio, eu pretium</li>
  </ul>
  <div class="btn btn-facilities">More Facilities <span>····›</span></div>
</section>

<section class="abs box box-diseases">
  <h2>Diseases &amp; Solution</h2>
  <div class="disease-photo" role="img" aria-label="Photo of a patient beside an eye scan monitor"></div>
  <p class="disease-text">Lorem ipsum dolor sit amet, consectetur adipiscing elit. Ut aliquet lacus et dolor mollis bibendum. Mauris sodales magna vel erat porttitor vel hendrerit velit lacinia.</p>
  <div class="btn btn-solutions">More Solutions <span>····›</span></div>
</section>

<section class="abs box box-doctor">
  <h2>Book A Doctor</h2>
  <div class="field first">Your Name</div>
  <div class="field">Your Phone No</div>
  <div class="field">Your Email Id</div>
  <div class="field message">Your Message</div>
  <div class="btn btn-submit">Submit <span>····›</span></div>
</section>

<div class="abs footer-tab"></div>
<div class="abs footer"></div>

<div class="abs footer-col quick-links">
  <h3>Quick Links</h3>
  <ul><li>Home</li><li>Browse</li><li>Movies</li><li>Upload</li><li>Profile</li><li>Contact Us</li></ul>
</div>

<div class="abs footer-col newsletter">
  <h3>Subscribe Newsletters</h3>
  <div class="news-field">Your name</div>
  <div class="news-field">Your email id</div>
  <p class="news-text">Lorem ipsum dolor sit amet, consectetur adipiscing elit. Proin posuere ipsum sit amet urna bibendum iaculis. Etiam faucibus ultricies diam ac facilisis. Maecenas eleifend iaculis vulputate.</p>
  <div class="subscribe">Subscribe Now
    <svg width="20" height="20" viewBox="0 0 20 20"><circle cx="10" cy="10" r="8.5" fill="none" stroke="#fff" stroke-width="2"/><path d="M6 10h7M10 6.5l3.5 3.5-3.5 3.5" fill="none" stroke="#fff" stroke-width="2"/></svg>
  </div>
</div>

<div class="abs footer-col follow">
  <h3>Follow Us</h3>
  <div class="social"><i></i><i></i><i></i><i></i></div>
  <h3 class="contact-title">Contact Us</h3>
  <div class="contact-line">
    <svg width="22" height="22" viewBox="0 0 24 24"><path d="M6.6 10.8a15 15 0 0 0 6.6 6.6l2.2-2.2a1 1 0 0 1 1-.25 11.4 11.4 0 0 0 3.6.57 1 1 0 0 1 1 1V20a1 1 0 0 1-1 1A17 17 0 0 1 3 4a1 1 0 0 1 1-1h3.5a1 1 0 0 1 1 1c0 1.25.2 2.45.57 3.6a1 1 0 0 1-.25 1z" fill="#e0322b"/></svg>
    555 0100 234
  </div>
  <div class="contact-line email">
    <svg width="24" height="18" viewBox="0 0 24 18"><rect x="1" y="1" width="22" height="16" rx="2" fill="#4fd0f5"/><path d="M1 2l11 8 11-8" fill="none" stroke="#0a5874" stroke-width="1.5"/></svg>
    info@brightfield.example
  </div>
</div>

<div class="abs footer-rule"></div>
<div class="abs copyright">© 2011, All Rights Reserved, Privacy Policy &nbsp; | &nbsp; Terms &amp; Conditions &nbsp; | &nbsp; Sitemap</div>

</body>
</html>
```